Vehicle Signage

Please design a graphic layout for a Van signage to advertise the business

"Kestrel Vantage Systems"
the logo is in the attached files

Also attached are some icons that represent the fields of service, I would like to use these in the design please
Updates

Reason: I am making some changes to the KVS logo to help match the Vans, I will up load the new files as soon as possible

Target Market(s)

We are targeting people who feel they would like to have some security equipment installed for piece of mind in the the fields of:
"Alarms, Intercoms, CCTV, Access Control"

Industry/Entity Type

Business

Requirements
Must have
• Must be Clear what we do,
it can be icons/pictures or words to represent the service areas of:

```html
<!DOCTYPE html>
<html lang="en">
<head>
<meta charset="utf-8">
<title>Kestrel Vantage Systems – Van Signage</title>
<link href="https://fonts.googleapis.com/css2?family=Montserrat:wght@600;700;800&display=swap" rel="stylesheet">
<style>
  :root {
    --backdrop: #c9cdd1;
    --strip: #e6e8ea;
    --navy: #0a2547;
    --cyan: #2aa8e0;
    --white: #ffffff;
  }
  html, body {
    margin: 0;
    padding: 0;
    width: 1200px;
    height: 901px;
    overflow: hidden;
    background: var(--backdrop);
    font-family: "Montserrat", Arial, sans-serif;
  }
  .signage {
    position: absolute;
    left: 60px;
    top: 270px;
    width: 1080px;
  }
  .services {
    height: 60px;
    background: var(--strip);
    color: var(--navy);
    font-weight: 700;
    font-size: 31px;
    letter-spacing: 1px;
    display: flex;
    align-items: center;
    justify-content: center;
    gap: 20px;
    white-space: nowrap;
  }
  .brand-panel {
    height: 223px;
    background: var(--navy);
    display: flex;
    align-items: center;
    padding: 0 40px 0 44px;
    box-sizing: border-box;
  }
  .brand {
    width: 430px;
    display: flex;
    flex-direction: column;
  }
  .brand-name {
    font-weight: 800;
    font-size: 128px;
    line-height: 1;
    color: var(--cyan);
    letter-spacing: 4px;
  }
  .brand-tagline {
    font-weight: 800;
    font-size: 20px;
    color: var(--cyan);
    letter-spacing: 0.5px;
    margin-top: 10px;
    white-space: nowrap;
  }
  .service-icons {
    flex: 1;
    display: flex;
    justify-content: space-between;
    align-items: center;
  }
  .service-icons svg {
    width: 120px;
    height: 120px;
    fill: var(--cyan);
  }
  .contact {
    height: 70px;
    display: flex;
    align-items: center;
    padding-left: 72px;
    gap: 16px;
    color: var(--navy);
    font-weight: 700;
    font-size: 28px;
    letter-spacing: 1px;
    white-space: nowrap;
  }
  .contact > * { flex-shrink: 0; }
  .contact svg {
    width: 32px;
    height: 32px;
    fill: var(--navy);
  }
</style>
</head>
<body>
  <section class="signage">
    <div class="services">
      <span>ALARMS</span><span>INTERCOMS</span><span>CCTV</span><span>ACCESS CONTROL</span><span>ALARMS</span>
    </div>

    <div class="brand-panel">
      <div class="brand">
        <div class="brand-name">KVS</div>
        <div class="brand-tagline">KESTREL VANTAGE SYSTEMS</div>
      </div>

      <div class="service-icons">
        <svg class="icon-camera" viewBox="0 0 100 100" aria-label="CCTV camera">
          <path d="M10 38 L70 20 L78 46 L18 64 Z"/>
          <path d="M72 40 L86 36 L88 44 L75 48 Z"/>
          <rect x="38" y="58" width="8" height="20"/>
          <rect x="26" y="76" width="40" height="8"/>
          <rect x="6" y="60" width="6" height="28"/>
        </svg>

        <svg class="icon-siren" viewBox="0 0 100 100" aria-label="Alarm siren">
          <path d="M30 80 L30 58 A20 20 0 0 1 70 58 L70 80 Z"/>
          <rect x="20" y="82" width="60" height="10"/>
          <rect x="46" y="14" width="8" height="18"/>
          <rect x="6" y="52" width="16" height="7"/>
          <rect x="78" y="52" width="16" height="7"/>
          <path d="M18 26 L24 20 L34 32 L28 37 Z"/>
          <path d="M82 26 L76 20 L66 32 L72 37 Z"/>
        </svg>

        <svg class="icon-keypad" viewBox="0 0 100 100" aria-label="Access keypad">
          <circle cx="22" cy="14" r="6"/><circle cx="40" cy="14" r="6"/><circle cx="58" cy="14" r="6"/>
          <circle cx="22" cy="32" r="6"/><circle cx="40" cy="32" r="6"/><circle cx="58" cy="32" r="6"/>
          <circle cx="22" cy="50" r="6"/><circle cx="58" cy="50" r="6"/>
          <path d="M36 48 A5 5 0 0 1 46 48 L46 64 L70 66 A8 8 0 0 1 78 74 L76 96 L44 96 L30 78 A5 5 0 0 1 38 72 L36 70 Z"/>
        </svg>

        <svg class="icon-speaker" viewBox="0 0 100 100" aria-label="Intercom speaker">
          <path d="M8 38 L26 38 L50 18 L50 82 L26 62 L8 62 Z"/>
          <path d="M60 36 A18 18 0 0 1 60 64 L56 59 A11 11 0 0 0 56 41 Z"/>
          <path d="M68 24 A34 34 0 0 1 68 76 L63 71 A27 27 0 0 0 63 29 Z"/>
          <path d="M78 12 A50 50 0 0 1 78 88 L73 83 A43 43 0 0 0 73 17 Z"/>
        </svg>
      </div>
    </div>

    <div class="contact">
      <svg viewBox="0 0 24 24" aria-label="Phone">
        <path d="M6.6 10.8a15 15 0 0 0 6.6 6.6l2.2-2.2a1 1 0 0 1 1-.25 11.4 11.4 0 0 0 3.6.57 1 1 0 0 1 1 1V20a1 1 0 0 1-1 1A17 17 0 0 1 3 4a1 1 0 0 1 1-1h3.5a1 1 0 0 1 1 1c0 1.25.2 2.45.57 3.57a1 1 0 0 1-.25 1z"/>
      </svg>
      <span class="contact-phone">0400 555 192</span>
      <span class="contact-web">WWW.KVSYSTEMS.AU</span>
      <span class="contact-name">KESTREL VANTAGE</span>
    </div>
  </section>
</body>
</html>
```